Letterhead Design Project

Please see attached logo as well as information below which could be relevant to design. Let me know if you have any questions.

Derek J. Vollman
Estate Planning and Insurance Specialist
Dvollman@vollmanadvisory.com
P: 516-298-4153 F: 516-298-4187
www.vollmanadvisory.com
4150 Brindlemoor Parkway, Suite 317E
Syosset, New York 11804

Insurance

```html
<!DOCTYPE html>
<html lang="en">
<head>
<meta charset="utf-8">
<title>Vollman Advisory Group — Stationery</title>
<link href="https://fonts.googleapis.com/css2?family=Roboto+Condensed:wght@300;400&family=Cinzel:wght@400&display=swap" rel="stylesheet">
<style>
  :root {
    --navy: #1f2230;
    --gold: #cdb98a;
    --gold-faint: #ede5d2;
    --paper: #ffffff;
    --ink: #2b2b2b;
    --stage: #e9e6e1;
    --label: #1a1a1a;
    --card-text: #e3e3e3;
  }
  * { box-sizing: border-box; margin: 0; padding: 0; }
  html, body { width: 1200px; height: 733px; overflow: hidden; }
  body {
    position: relative;
    background: var(--stage);
    font-family: "Roboto Condensed", "Arial Narrow", sans-serif;
    color: var(--ink);
  }
  .sheet, .card, .envelope, .view-label { position: absolute; }
  address { font-style: normal; }

  /* brand lockup */
  .brand { display: flex; align-items: center; gap: 8px; color: var(--gold); }
  .brand-square { width: 38px; height: 38px; border: 2px solid var(--gold); flex: none; }
  .brand-name {
    font-family: "Roboto Condensed", sans-serif;
    font-weight: 300;
    font-size: 20px;
    letter-spacing: 2px;
    text-transform: uppercase;
    white-space: nowrap;
  }

  /* letterhead */
  .letterhead { left: 21px; top: 38px; width: 518px; height: 670px; background: var(--paper); }
  .letterhead .header-band { position: absolute; left: 0; top: 11px; width: 444px; height: 69px; background: var(--navy); display: flex; align-items: center; padding-left: 25px; }
  .letterhead .header-accent { position: absolute; left: 451px; top: 11px; width: 67px; height: 69px; background: var(--gold); }
  .letterhead .emblem {
    position: absolute; left: 165px; top: 253px; width: 188px; height: 188px;
    display: flex; flex-direction: column; align-items: center; justify-content: center; gap: 14px;
    color: var(--gold-faint);
  }
  .letterhead .emblem-square { width: 110px; height: 110px; border: 8px solid var(--gold-faint); }
  .letterhead .emblem-name { font-weight: 300; font-size: 22px; letter-spacing: 4px; text-transform: uppercase; white-space: nowrap; }
  .contact-list { list-style: none; font-size: 10.5px; line-height: 14px; }
  .contact-list li { display: flex; align-items: center; gap: 4px; white-space: nowrap; }
  .contact-list svg { width: 8px; height: 8px; flex: none; }
  .letterhead .contact-list { position: absolute; left: 24px; top: 610px; }
  .letterhead .address { position: absolute; left: 402px; top: 616px; font-size: 10.5px; line-height: 12.5px; }

  /* business cards */
  .view-label { font-family: "Roboto Condensed", sans-serif; font-size: 10px; color: var(--label); width: 213px; text-align: center; }
  .card { width: 213px; height: 121px; border-radius: 8px; background: var(--navy); overflow: hidden; }
  .card.gold { background: var(--gold); }
  .card .brand { gap: 5px; }
  .card .brand-square { width: 20px; height: 20px; border-width: 1.5px; }
  .card .brand-name { font-size: 9.5px; letter-spacing: 0.8px; }
  .card.gold .brand { color: var(--navy); }
  .card.gold .brand-square { border-color: var(--navy); }
  .card .site { position: absolute; left: 0; right: 0; bottom: 18px; text-align: center; font-size: 7px; letter-spacing: 1.2px; color: #d9d9d9; }
  .card.gold .site { color: var(--navy); }
  .card-front .brand { position: absolute; left: 21px; top: 23px; }
  .card-front .name-bar { position: absolute; left: 0; top: 58px; width: 184px; height: 14px; background: var(--gold); display: flex; align-items: center; padding-left: 10px; gap: 3px; color: var(--navy); white-space: nowrap; }
  .card-front .holder { font-family: "Cinzel", serif; font-size: 7.5px; }
  .card-front .role { font-size: 5.4px; }
  .card-front .name-tail { position: absolute; left: 185px; top: 58px; width: 28px; height: 14px; background: var(--paper); }
  .card-front .contact-list { position: absolute; left: 20px; top: 79px; font-size: 5.6px; line-height: 8.7px; color: var(--card-text); }
  .card-front .contact-list svg { width: 5px; height: 5px; }
  .card-front .address { position: absolute; left: 122px; top: 91px; font-size: 5.6px; line-height: 7px; color: var(--card-text); white-space: nowrap; }
  .card-back .brand { position: absolute; left: 20px; top: 45px; }
  .card-stacked .brand { position: absolute; left: 0; right: 0; top: 16px; flex-direction: column; gap: 6px; }
  .card-stacked .brand-square { width: 46px; height: 46px; border-width: 2px; }
  .card-stacked .brand-name { font-size: 10px; letter-spacing: 1.2px; }

  /* envelope */
  .envelope { left: 597px; top: 390px; width: 579px; height: 318px; }
  .envelope .flap { position: absolute; left: 0; top: 0; width: 579px; height: 68px; }
  .envelope .flap-mark { position: absolute; left: 272px; top: 12px; width: 38px; height: 38px; border: 2px solid var(--gold); }
  .envelope .body { position: absolute; left: 0; top: 68px; width: 579px; height: 250px; background: var(--paper); }
  .envelope .header-band { position: absolute; left: 0; top: 19px; width: 497px; height: 68px; background: var(--navy); display: flex; align-items: center; padding-left: 34px; }
  .envelope .header-accent { position: absolute; left: 504px; top: 19px; width: 75px; height: 68px; background: var(--gold); }
  .envelope .brand-square { width: 42px; height: 42px; }
  .envelope .brand-name { font-size: 18px; }
  .envelope .address { position: absolute; left: 43px; top: 100px; font-size: 10.5px; line-height: 12.5px; }
  .envelope .site { position: absolute; left: 49px; bottom: 18px; font-size: 10.5px; letter-spacing: 1.4px; }
</style>
</head>
<body>

  <section class="sheet letterhead" aria-label="Letterhead">
    <header class="header-band">
      <div class="brand"><span class="brand-square"></span><span class="brand-name">Vollman Advisory Group</span></div>
    </header>
    <div class="header-accent"></div>
    <div class="emblem" aria-hidden="true">
      <span class="emblem-square"></span>
      <span class="emblem-name">Vollman</span>
    </div>
    <ul class="contact-list">
      <li><svg viewBox="0 0 10 10"><path d="M2 1l2 2-1 1.5c.7 1.4 1.6 2.3 3 3L7.5 6l2 2-1.5 1.5C4.5 9 1 5.5.5 2.5z" fill="#333"/></svg>516-298-4153</li>
      <li><svg viewBox="0 0 10 10"><rect x="1" y="4" width="8" height="5" fill="#333"/><rect x="2.5" y="1" width="5" height="3" fill="#333"/></svg>516-298-4187</li>
      <li><svg viewBox="0 0 10 10"><circle cx="5" cy="5" r="4" fill="none" stroke="#333"/><path d="M1 5h8M5 1v8" stroke="#333" stroke-width=".8"/></svg>www.vollmanadvisory.com</li>
    </ul>
    <address class="address">4150 Brindlemoor Parkway<br>Suite 317E, Syosset<br>New York 11804</address>
  </section>

  <span class="view-label" style="left:676px;top:4px">Front</span>
  <article class="card card-front" style="left:676px;top:21px" aria-label="Business card front">
    <div class="brand"><span class="brand-square"></span><span class="brand-name">Vollman Advisory Group</span></div>
    <div class="name-bar"><span class="holder">Derek J. Vollman,</span><span class="role">Estate Planning and Insurance Specialist</span></div>
    <div class="name-tail"></div>
    <ul class="contact-list">
      <li><svg viewBox="0 0 10 10"><circle cx="5" cy="5" r="4" fill="#e3e3e3"/></svg>516-298-4153</li>
      <li><svg viewBox="0 0 10 10"><rect x="1" y="3" width="8" height="6" fill="#e3e3e3"/></svg>516-298-4187</li>
      <li><svg viewBox="0 0 10 10"><rect x="1" y="2" width="8" height="6" fill="none" stroke="#e3e3e3"/></svg>Dvollman@vollmanadvisory.com</li>
      <li><svg viewBox="0 0 10 10"><circle cx="5" cy="5" r="4" fill="none" stroke="#e3e3e3"/></svg>www.vollmanadvisory.com</li>
    </ul>
    <address class="address">4150 Brindlemoor Parkway<br>Suite 317E, Syosset<br>New York 11804</address>
  </article>

  <span class="view-label" style="left:910px;top:5px">Back - 1</span>
  <article class="card card-back" style="left:910px;top:22px" aria-label="Business card back, dark">
    <div class="brand"><span class="brand-square"></span><span class="brand-name">Vollman Advisory Group</span></div>
    <p class="site">www.vollmanadvisory.com</p>
  </article>

  <span class="view-label" style="left:675px;top:154px">Back - 2</span>
  <article class="card card-stacked" style="left:675px;top:171px" aria-label="Business card back, stacked">
    <div class="brand"><span class="brand-square"></span><span class="brand-name">Vollman Advisory</span></div>
    <p class="site" style="bottom:6px;color:var(--gold)">www.vollmanadvisory.com</p>
  </article>

  <span class="view-label" style="left:910px;top:154px">Back - 3</span>
  <article class="card card-back gold" style="left:910px;top:171px" aria-label="Business card back, gold">
    <div class="brand"><span class="brand-square"></span><span class="brand-name">Vollman Advisory Group</span></div>
    <p class="site">www.vollmanadvisory.com</p>
  </article>

  <section class="envelope" aria-label="Envelope">
    <svg class="flap" viewBox="0 0 579 68" aria-hidden="true">
      <path d="M0 68 L30 8 Q34 0 44 0 L534 0 Q546 0 550 8 L579 68 Z" fill="var(--navy)"/>
    </svg>
    <span class="flap-mark"></span>
    <div class="body">
      <header class="header-band">
        <div class="brand"><span class="brand-square"></span><span class="brand-name">Vollman Advisory Group</span></div>
      </header>
      <div class="header-accent"></div>
      <address class="address">4150 Brindlemoor Parkway<br>Suite 317E, Syosset, New York 11804</address>
      <p class="site">www.vollmanadvisory.com</p>
    </div>
  </section>

</body>
</html>
```